Book Cover for nonfiction book about defeating one's grief

I need a book cover (front and back) for a book titled Senderos de Sauces (Willow Paths). I have included a word document of the back cover copy. I liked the design of When the river turns (http://www.pixelvarno.com/design/4817302) so something like that would be nice. But if you have a better idea that's fine.
Target Market(s)
People suffering from the loss of a loved one
Requirements
Must have
- Please move the author information (which is the first paragraph) so that it is the last paragraph
- Please include my middle initial in the name (Derek T. Fenwick)
- 6 x 9 inch book, 9mm spine width, 5cm x 3 cm UPC placeholder on back cover
- Thanks!
Nice to have
- should convey relief from grief or some one grieving

```html
<!DOCTYPE html>
<html lang="es">
<head>
<meta charset="utf-8">
<title>Senderos de Sauces — Derek T. Fenwick</title>
<link rel="stylesheet" href="https://fonts.googleapis.com/css2?family=Marcellus+SC&family=Carlito&display=swap">
<style>
  :root {
    --sky-top: #86cbc6;
    --sky-mid: #b8ded8;
    --sky-low: #e2f1ec;
    --cloud: #f4f8f4;
    --meadow: #5f7a26;
    --bloom: #e3c136;
    --red-deep: #8e1616;
    --red-bright: #dc2a2a;
    --band: #d42528;
    --band-dark: #8f1b1b;
    --white: #ffffff;
    --rule: #3a3a3a;
    --figure-light: #f3efe6;
    --figure-skin: #d9a98a;
    --figure-dark: #3a2a26;
  }
  * { margin: 0; padding: 0; box-sizing: border-box; }
  html, body { width: 1200px; height: 862px; overflow: hidden; background: #fff; }
  .cover {
    position: relative; width: 1200px; height: 862px; overflow: hidden;
    font-family: "Carlito", "Calibri", sans-serif;
  }
  .cover-art, .front-photo { position: absolute; left: 0; top: 0; }
  .back-title {
    position: absolute; left: 62px; top: 62px; width: 440px;
    font-family: "Marcellus SC", serif; font-weight: 400; font-size: 34px; color: var(--red-deep);
    letter-spacing: 1px; text-align: center; white-space: nowrap;
  }
  .blurb {
    position: absolute; left: 58px; width: 452px;
    font-size: 13.6px; line-height: 22px; color: var(--red-deep);
    text-align: justify;
  }
  .blurb .accent { color: var(--red-bright); }
  .blurb-one { top: 120px; }
  .blurb-two { top: 258px; }
  .blurb-three { top: 410px; }
  .author-bio { top: 580px; text-align: center; left: 70px; width: 430px; }
  .rule { position: absolute; left: 85px; width: 382px; height: 1px; background: var(--rule); }
  .rule-one { top: 397px; }
  .rule-two { top: 566px; }
  .spine-text {
    position: absolute; left: 576px; top: 60px; height: 740px;
    writing-mode: vertical-rl;
    font-family: "Marcellus SC", serif; font-size: 33px; color: var(--red-deep);
    letter-spacing: 1.5px; white-space: nowrap;
  }
  .front-title {
    position: absolute; left: 640px; top: 40px; width: 560px;
    font-family: "Marcellus SC", serif; font-weight: 400; text-align: center; line-height: 1;
    background: linear-gradient(90deg, var(--red-deep), var(--red-bright) 55%, var(--red-deep));
    -webkit-background-clip: text; background-clip: text; color: transparent;
  }
  .front-title .line-lg { display: block; font-size: 78px; letter-spacing: 1px; }
  .front-title .line-sm { display: block; font-size: 50px; margin: 10px 0 8px; }
  .bottom-band {
    position: absolute; left: 0; top: 788px; width: 1200px; height: 54px;
    background: linear-gradient(90deg, var(--band-dark), var(--band) 25%, var(--band) 80%, var(--band-dark));
  }
  .front-author {
    position: absolute; left: 640px; width: 560px; top: 798px; text-align: center;
    font-family: "Marcellus SC", serif; font-size: 31px; color: var(--white); letter-spacing: 2.5px;
  }
  .upc-placeholder {
    position: absolute; left: 318px; top: 707px; width: 195px; height: 114px; background: var(--white);
  }
</style>
</head>
<body>
<main class="cover">
  <svg class="cover-art" width="1200" height="862" viewBox="0 0 1200 862" role="img"
       aria-label="Photograph of a bright blue sky with soft white clouds above a meadow full of yellow dandelions">
    <defs>
      <linearGradient id="sky" x1="0" y1="0" x2="0" y2="1">
        <stop offset="0" stop-color="var(--sky-top)"/>
        <stop offset="0.55" stop-color="var(--sky-mid)"/>
        <stop offset="0.85" stop-color="var(--sky-low)"/>
      </linearGradient>
      <radialGradient id="glow" cx="0.5" cy="0.5" r="0.5">
        <stop offset="0" stop-color="var(--cloud)" stop-opacity="0.85"/>
        <stop offset="1" stop-color="var(--cloud)" stop-opacity="0"/>
      </radialGradient>
      <linearGradient id="meadow" x1="0" y1="0" x2="0" y2="1">
        <stop offset="0" stop-color="var(--meadow)"/>
        <stop offset="0.55" stop-color="var(--bloom)"/>
        <stop offset="1" stop-color="var(--meadow)"/>
      </linearGradient>
    </defs>
    <rect width="1200" height="862" fill="url(#sky)"/>
    <ellipse cx="500" cy="260" rx="420" ry="190" fill="url(#glow)"/>
    <ellipse cx="1020" cy="470" rx="230" ry="120" fill="url(#glow)"/>
    <ellipse cx="150" cy="690" rx="220" ry="80" fill="url(#glow)"/>
    <rect y="712" width="1200" height="150" fill="url(#meadow)"/>
  </svg>

  <svg class="front-photo" width="1200" height="862" viewBox="0 0 1200 862" role="img"
       aria-label="Photograph of a joyful young woman leaping barefoot with both arms raised to the sky above the dandelion meadow, expressing relief and freedom">
    <defs>
      <linearGradient id="figure" x1="0" y1="0" x2="0" y2="1">
        <stop offset="0" stop-color="var(--figure-light)" stop-opacity="0.15"/>
        <stop offset="0.35" stop-color="var(--figure-light)" stop-opacity="0.75"/>
        <stop offset="0.6" stop-color="var(--figure-dark)" stop-opacity="0.55"/>
        <stop offset="1" stop-color="var(--figure-skin)" stop-opacity="0.35"/>
      </linearGradient>
    </defs>
    <rect x="700" y="370" width="270" height="340" rx="135" fill="url(#figure)"/>
  </svg>

  <h2 class="back-title">SENDEROS DE SAUCES</h2>

  <p class="blurb blurb-one">Por miles de años, se le ha dicho a la humanidad que el dolor es una parte necesaria de la vida, y que el profundo dolor después del fallecimiento de nuestros seres queridos es esperado y un proceso natural. Derek Fenwick dice enfáticamente que no, ¡no lo es! <span class="accent">Puedes, y deberías estar emocionalmente estable y espiritualmente contento después de la muerte de un ser querido.</span></p>

  <p class="blurb blurb-two">La gente a veces pasa meses o años sumidos en el dolor paralizante, lo cual los aparta de muchos esfuerzos fructíferos. El dolor sabotea las vidas felices y productivas. <span class="accent">Algunas veces la gente que trata con dolor extremo o pérdidas, se convierten en personas enojadas, abusan de las drogas y alcohol o incluso de quitan sus propias vidas.</span> No debe ser de esta manera. La tristeza, cuando alguien se va de nuestras vidas, es normal. No es necesario sufrir siempre.</p>

  <div class="rule rule-one"></div>

  <p class="blurb blurb-three"><span class="accent">La muerte, como parte de la vida, era una norma en la vida de cualquier persona normal.</span> Ahora es raras veces discutida y solo cuando ocurre una emergencia. Senderos de Sauces es una franca discusión sobre la muerte y morir significa traer paz a los corazones de aquellas personas que están en duelo y esas personas que temen su propia muerte. <span class="accent">No es insensible, oscuro y fuerte de leer pero es positivo, reconfortante y espiritualmente tranquilizador.</span></p>

  <div class="rule rule-two"></div>

  <p class="blurb author-bio">Derek Fenwick se graduó de la <span class="accent">Universidad Lago Norte</span> y desde entonces ha vivido en Nueva Jersey trabajando como editor y escritor en el mercado de masas, tecnología y los campos de educación. Él es autor de otros tres libros de los que pueden encontrar más en <span class="accent">DerekTFenwick.com</span></p>

  <div class="spine-text">SENDEROS DE SAUCES &nbsp;&nbsp;DEREK T. FENWICK</div>

  <h1 class="front-title">
    <span class="line-lg">SENDEROS</span>
    <span class="line-sm">DE</span>
    <span class="line-lg">SAUCES</span>
  </h1>

  <div class="bottom-band"></div>
  <div class="front-author">DEREK T. FENWICK</div>
  <div class="upc-placeholder"></div>
</main>
</body>
</html>
```